Wordpress Web Design & Coding for velnoragroup.ca

We need a website for a new investment company that is visually grabbing and vibrant. We would like to see a web page that displays trust, growth and confidence. Needs to be responsive and mobile friendly for all browsers and coded for both Android & IOS.

Open to the number of pages and menu items. I selected 4 but if you feel the layout would work better with less I am open to this. Need to sell the people (management team/related businesses) and then show where the invested money will be going (upcoming projects).

Company Info:

Velnora is an investment company put together by a group of seasoned business professionals who have come together to combine decades of success in the real estate development, management, financing and medical services. The company will be a full service company offering turn key solutions for medical professionals.

Vel-Nora will focus on providing a full range of services via a group of distinct companies to deliver newly emerging needs of the medical community. The end goal will be to create complete solutions for individuals in the medical community. Our group has experience and success with the conceptualization, construction and financing of medical and dental clinic spaces. Vel-Nora Group will be established to accommodate all areas of the development and creation of clinics for medical professionals from building construction to equipment financing and administrations.

You can mention these companies and take photos from their websites. You can also use stock photos.

Our construction partner:
https://382bld.com/projects/

Our equipment leasing partner:
https://www.pordiva.com/

Our Management Team and medical partners

Gil Parkes
https://www.mysoundpoise.ca/

Milos Vendraker
https://www.qrtdentalservices.com/about-us

PROPOSED PROJECTS (see attachment for details)
Hollowmere Business Park
Cresfield Business Park
Mt. Corwin Ridge Professional

Investors

Investment

Sans Serif

Must have
• Wordpress – must be both desktop and mobile friendly with fast page load speed
Ability to edit after ourselves in Wordpress
Attractive home page with logo etc.
Logo colours are: for the blue the pantone color is #0355a3
and for the green is #8cc63f

Sections, about us, what we do/services we provide, contact us

```html
<!DOCTYPE html>
<html lang="en">
<head>
<meta charset="utf-8">
<title>Vel-Nora Group</title>
<link href="https://fonts.googleapis.com/css2?family=Montserrat:wght@300;400;500;600;700&family=Open+Sans:wght@400;600&display=swap" rel="stylesheet">
<style>
:root{
  --blue:#0355a3;
  --green:#8cc63f;
  --ink:#1b1b1b;
  --text:#6a6a6a;
  --grey-bg:#f4f4f4;
  --white:#ffffff;
}
*{box-sizing:border-box;margin:0;padding:0}
html,body{width:1200px;height:3767px;overflow:hidden;background:var(--white)}
body{position:relative;font-family:"Open Sans",Arial,sans-serif;color:var(--text)}
.abs{position:absolute}
.heading{font-family:"Montserrat",Arial,sans-serif;font-weight:700;color:var(--ink)}
.section-title{position:absolute;left:0;width:1200px;text-align:center;font-family:"Montserrat",Arial,sans-serif;font-weight:700;font-size:31px;color:var(--ink)}
.title-rule{position:absolute;left:564px;width:72px;height:2px;background:var(--blue)}

/* header */
.site-header{position:absolute;top:0;left:0;width:1200px;height:91px;background:var(--white)}
.brand{position:absolute;display:flex;align-items:center;gap:7px;font-family:"Montserrat",Arial,sans-serif;font-weight:700;color:var(--blue);font-size:15px;letter-spacing:.3px;white-space:nowrap}
.brand-mark{width:12px;height:12px;background:var(--green);flex:none}
.main-nav{position:absolute;left:365px;top:37px;display:flex;gap:28px;font-family:"Montserrat",Arial,sans-serif;font-size:12.5px;color:#222;letter-spacing:.3px}
.search-btn{position:absolute;left:989px;top:32px;width:27px;height:27px;background:var(--blue)}

/* hero */
.hero{position:absolute;top:91px;left:0;width:1200px;height:508px;background:linear-gradient(180deg,#6d7a6a 0%,#8a8676 35%,#9a8f7e 60%,#6f6c66 100%)}
.hero-shade{position:absolute;inset:0;background:rgba(20,20,20,.28)}
.hero-title{position:absolute;top:176px;left:0;width:1200px;text-align:center;font-family:"Montserrat",Arial,sans-serif;font-weight:400;font-size:38px;line-height:47px;color:var(--white);letter-spacing:.8px}

/* about */
.about-title{left:172px;top:671px;font-size:32px}
.about-text{left:172px;top:729px;width:343px;font-size:13.8px;line-height:18px;text-align:justify;color:var(--text)}
.btn{position:absolute;display:flex;align-items:center;justify-content:center;background:var(--blue);color:var(--white);font-family:"Montserrat",Arial,sans-serif;font-weight:600;font-size:12.5px}
.photo{position:absolute}

/* services */
.service{position:absolute;top:1150px;width:196px;text-align:center}
.service svg{display:block;margin:0 auto}
.service-name{margin-top:32px;font-family:"Montserrat",Arial,sans-serif;font-weight:600;font-size:14px;color:var(--ink)}
.service-rule{width:50px;height:2px;background:var(--blue);margin:20px auto 0}
.service-text{margin-top:30px;text-align:justify;font-size:13px;line-height:18px;color:var(--text)}

/* projects */
.projects{position:absolute;top:1440px;left:0;width:1200px;height:901px;background:var(--grey-bg)}
.project-name{position:absolute;font-family:"Montserrat",Arial,sans-serif;font-weight:600;font-size:19px;color:var(--blue)}
.project-text{position:absolute;font-size:12.3px;line-height:20px;text-align:justify;color:#444}
.more-link{position:absolute;font-family:"Montserrat",Arial,sans-serif;font-weight:600;font-size:12.5px;color:var(--ink);display:flex;align-items:center;gap:8px}
.more-link::after{content:"";border-left:5px solid var(--ink);border-top:4px solid transparent;border-bottom:4px solid transparent}

/* partners */
.partner{position:absolute;top:2512px;width:197px;height:303px;background:var(--blue)}
.partner-photo{position:absolute;top:0;left:0;width:197px;height:169px}
.partner-role{position:absolute;left:12px;top:192px;width:175px;font-family:"Montserrat",Arial,sans-serif;font-size:15px;line-height:21px;color:var(--white)}
.partner-name{position:absolute;left:10px;top:241px;font-family:"Montserrat",Arial,sans-serif;font-size:13px;color:var(--white)}
.partner-more{position:absolute;right:12px;top:271px;font-family:"Montserrat",Arial,sans-serif;font-size:12.5px;color:var(--green)}

/* contact */
.contact{position:absolute;top:2958px;left:0;width:1200px;height:513px;background:linear-gradient(100deg,#6fa23a 0%,#86bc4c 45%,#9ccf5c 100%)}
.contact .section-title{color:var(--white)}
.field{position:absolute;left:246px;width:708px;border:1.5px solid rgba(255,255,255,.45);background:rgba(255,255,255,.06);color:#f0f6e6;font-family:"Montserrat",Arial,sans-serif;font-size:12px;padding:0 0 0 20px}
.submit{position:absolute;left:246px;top:398px;width:708px;height:38px;background:var(--white);display:flex;align-items:center;justify-content:center;font-family:"Montserrat",Arial,sans-serif;font-weight:600;font-size:13px;color:var(--ink)}

/* footer */
.site-footer{position:absolute;top:3471px;left:0;width:1200px;height:296px;background:var(--blue)}
.footer-brand{position:absolute;top:55px;left:0;width:1200px;display:flex;justify-content:center;align-items:center;gap:8px;font-family:"Montserrat",Arial,sans-serif;font-weight:700;font-size:20px;color:var(--white);letter-spacing:.5px}
.social{position:absolute;top:128px;left:0;width:1200px;display:flex;justify-content:center;gap:16px}
.social span{width:12px;height:12px;border-radius:50%;background:var(--white)}
.footer-nav{position:absolute;top:173px;left:0;width:1200px;display:flex;justify-content:center;gap:28px;font-family:"Montserrat",Arial,sans-serif;font-size:12px;color:var(--white);letter-spacing:.3px}
.copyright{position:absolute;top:211px;left:0;width:1200px;text-align:center;font-size:11.5px;color:var(--white)}
</style>
</head>
<body>

<header class="site-header">
  <div class="brand" style="left:172px;top:37px"><span class="brand-mark"></span>VEL-NORA GROUP</div>
  <nav class="main-nav">
    <span>HOME</span><span>ABOUT US</span><span>WHAT WE DO</span><span>PROPOSED PROJECTS</span><span>TEAM</span><span>CONTACT US</span>
  </nav>
  <div class="search-btn">
    <svg width="27" height="27" viewBox="0 0 27 27"><circle cx="12.5" cy="12.5" r="4" fill="none" stroke="#fff" stroke-width="1.8"/><line x1="15.5" y1="15.5" x2="18.5" y2="18.5" stroke="#fff" stroke-width="2"/></svg>
  </div>
</header>

<section class="hero" role="img" aria-label="Aerial photograph of a large clinic building under construction">
  <div class="hero-shade"></div>
  <h1 class="hero-title">Providing a full range of services<br>to deliver newly emerging needs<br>of the medical community</h1>
</section>

<section class="about">
  <h2 class="abs heading about-title">About Us</h2>
  <p class="abs about-text">Velnora is an investment company put together by a group of seasoned business professionals who have come together to combine decades of success in the real estate development, management, financing and medical services. The company will be a full service company offering turn key solutions for medical professionals.</p>
  <div class="btn" style="left:172px;top:886px;width:125px;height:48px">Learn More</div>
  <div class="photo" role="img" aria-label="Red dental chair" style="left:557px;top:656px;width:161px;height:106px;background:linear-gradient(135deg,#d9d2c8,#c9485a 55%,#8e6a4c)"></div>
  <div class="photo" role="img" aria-label="Operating room with surgical lights" style="left:723px;top:656px;width:161px;height:161px;background:linear-gradient(180deg,#e6e9ec,#aab7c4 60%,#5d7390)"></div>
  <div class="photo" role="img" aria-label="Clinic building exterior with green lawn" style="left:889px;top:656px;width:124px;height:161px;background:linear-gradient(180deg,#dfe6ee,#c9ccd0 55%,#5f8a4a)"></div>
  <div class="photo" role="img" aria-label="Bright white waiting room" style="left:557px;top:767px;width:161px;height:164px;background:linear-gradient(135deg,#eef2f3,#c6d3d6 60%,#9aa9ad)"></div>
  <div class="photo" role="img" aria-label="Hospital corridor" style="left:723px;top:821px;width:161px;height:110px;background:linear-gradient(180deg,#f0f0ee,#c0c4c8 60%,#8a8f94)"></div>
  <div class="photo" role="img" aria-label="Hospital ward with blue beds" style="left:889px;top:821px;width:124px;height:110px;background:linear-gradient(180deg,#c9ced5,#4f78b8 70%,#2f4a78)"></div>
</section>

<section class="services">
  <h2 class="section-title" style="top:1050px">What We Do</h2>
  <div class="title-rule" style="top:1100px"></div>

  <div class="service" style="left:172px">
    <svg width="66" height="66" viewBox="0 0 66 66" fill="none" stroke="#0355a3" stroke-width="2"><rect x="22" y="6" width="26" height="38"/><path d="M27 12h4M35 12h4M27 19h4M35 19h4M27 26h4M35 26h4M27 33h4M35 33h4"/><path d="M4 46h12l10 4h14a4 4 0 0 1 0 6H26"/><path d="M16 60l12 2 26-10a4 4 0 0 0-4-6l-10 4"/></svg>
    <div class="service-name">Real Estate Development</div>
    <div class="service-rule"></div>
    <p class="service-text">Excepteur sint occaecat cupidatat non proident, sunt in culpa qui officia deserunt mollit anim id est laborum</p>
  </div>
  <div class="service" style="left:393px">
    <svg width="66" height="66" viewBox="0 0 66 66" fill="none" stroke="#0355a3" stroke-width="2"><circle cx="33" cy="26" r="20"/><circle cx="33" cy="20" r="5"/><path d="M24 34a9 9 0 0 1 18 0"/><circle cx="20" cy="26" r="3.5"/><circle cx="46" cy="26" r="3.5"/><path d="M6 44l12-6 10 6 8-4 10 4 14-6v10L46 56 34 62 20 56 6 54z"/></svg>
    <div class="service-name">Management</div>
    <div class="service-rule"></div>
    <p class="service-text">Excepteur sint occaecat cupidatat non proident, sunt in culpa qui officia deserunt mollit anim id est laborum</p>
  </div>
  <div class="service" style="left:612px">
    <svg width="66" height="66" viewBox="0 0 66 66" fill="none" stroke="#0355a3" stroke-width="2"><rect x="4" y="16" width="40" height="22" transform="rotate(-8 24 27)"/><rect x="6" y="22" width="40" height="22"/><circle cx="26" cy="33" r="6"/><path d="M26 30v6"/><ellipse cx="52" cy="40" rx="9" ry="3"/><path d="M43 40v18c0 2 4 3 9 3s9-1 9-3V40M43 46c0 2 4 3 9 3s9-1 9-3M43 52c0 2 4 3 9 3s9-1 9-3"/></svg>
    <div class="service-name">Financing</div>
    <div class="service-rule"></div>
    <p class="service-text">Excepteur sint occaecat cupidatat non proident, sunt in culpa qui officia deserunt mollit anim id est laborum</p>
  </div>
  <div class="service" style="left:832px">
    <svg width="66" height="66" viewBox="0 0 66 66" fill="none" stroke="#0355a3" stroke-width="2"><rect x="12" y="8" width="40" height="50"/><rect x="24" y="4" width="16" height="8"/><path d="M29 18h6v6h6v6h-6v6h-6v-6h-6v-6h6z"/><path d="M18 44h28M18 50h20"/><path d="M6 30l8 30h40l6-24"/></svg>
    <div class="service-name">Medical</div>
    <div class="service-rule"></div>
    <p class="service-text">Excepteur sint occaecat cupidatat non proident, sunt in culpa qui officia deserunt mollit anim id est laborum</p>
  </div>
</section>

<section class="projects">
  <h2 class="section-title" style="top:58px">Proposed Projects</h2>
  <div class="title-rule" style="top:110px;background:var(--ink)"></div>

  <div class="photo" role="img" aria-label="Rendering of a two storey business park building with tenant signage" style="left:172px;top:168px;width:418px;height:511px;background:linear-gradient(180deg,#5a5a66 0%,#9c9ca4 30%,#d8d8dc 50%,#7a7a80 80%,#b9b9bc 100%);border:1px solid #999"></div>
  <h3 class="project-name" style="left:171px;top:692px">Cresfield Business Park</h3>
  <p class="project-text" style="left:172px;top:729px;width:416px">The city of Cresfield is a core municipality in the Western Communities. It is currently experiencing regional increases in population driven by residential, commercial and industrial development...</p>
  <div class="more-link" style="left:172px;top:800px">Learn More</div>

  <div class="photo" role="img" aria-label="Black and white photos of a reception lobby and waiting area" style="left:618px;top:166px;width:418px;height:170px;background:linear-gradient(90deg,#3d3d3d,#a8a8a8 35%,#d5d5d5 55%,#6e6e6e 80%,#b0b0b0);border:1px solid #999"></div>
  <h3 class="project-name" style="left:620px;top:356px">Mt. Corwin Ridge Professional</h3>
  <p class="project-text" style="left:620px;top:389px;width:420px;line-height:19px">Mt. Corwin Ridge Professional building will feature a repurposed building adjacent to Mt. Corwin Ridge in Corwin, AB. This location served as a car dealership, but will be renovated from its current structure to a two storey building...</p>
  <div class="more-link" style="left:620px;top:474px">Learn More</div>

  <div class="photo" role="img" aria-label="Site plan drawing of the business park layout" style="left:620px;top:504px;width:416px;height:175px;background:linear-gradient(135deg,#e4e4e4,#d3d3d3 50%,#e8e8e8);border:1px solid #bbb"></div>
  <h3 class="project-name" style="left:619px;top:692px">Hollowmere Business Park</h3>
  <p class="project-text" style="left:620px;top:729px;width:418px">The Hollowmere Business Park in Cresfield, British Columbia on Tallis Island, is presently under contract with partners that are controlled by individuals who from part of the Vel-Nora management group...</p>
  <div class="more-link" style="left:621px;top:822px">Learn More</div>
</section>

<section class="partners">
  <h2 class="section-title" style="top:2399px">Our Partners</h2>
  <div class="title-rule" style="top:2448px"></div>

  <article class="partner" style="left:172px">
    <div class="partner-photo" role="img" aria-label="Glass office tower against blue sky" style="background:linear-gradient(135deg,#1f5fa8,#4d87c4 45%,#e6e9ee 70%,#9fb0c2)"></div>
    <div class="partner-role">Our construction partner</div>
    <div class="partner-more">Learn More</div>
  </article>
  <article class="partner" style="left:392px">
    <div class="partner-photo" role="img" aria-label="Hospital ward with rows of beds" style="background:linear-gradient(180deg,#e2e4e6,#b9c6d4 55%,#5f86b8)"></div>
    <div class="partner-role">Our equipment leasing partner</div>
    <div class="partner-more">Learn More</div>
  </article>
  <article class="partner" style="left:612px">
    <div class="partner-photo" role="img" aria-label="Portrait of Gil Parkes" style="background:linear-gradient(180deg,#7c7f84,#b59a86 55%,#4a4a50)"></div>
    <div class="partner-role">Management Team and medical partners</div>
    <div class="partner-name">Gil Parkes</div>
    <div class="partner-more">Learn More</div>
  </article>
  <article class="partner" style="left:832px">
    <div class="partner-photo" role="img" aria-label="Portrait of Milos Vendraker outdoors" style="background:linear-gradient(180deg,#e7eef3,#9fb7c6 40%,#b48a72 65%,#2f6f8a)"></div>
    <div class="partner-role">Management Team and medical partners</div>
    <div class="partner-name">Milos Vendraker</div>
    <div class="partner-more">Learn More</div>
  </article>
</section>

<section class="contact" role="img" aria-label="Green tinted photo of hands typing on a laptop">
  <h2 class="section-title" style="top:63px">Contact Us</h2>
  <div class="title-rule" style="top:111px;background:var(--white)"></div>
  <div class="field" style="top:158px;height:38px;line-height:35px">Name...</div>
  <div class="field" style="top:203px;height:39px;line-height:36px">Email...</div>
  <div class="field" style="top:250px;height:130px;padding-top:12px">Message...</div>
  <div class="submit">Submit</div>
</section>

<footer class="site-footer">
  <div class="footer-brand"><span class="brand-mark"></span>VEL-NORA GROUP</div>
  <div class="social"><span></span><span></span><span></span><span></span></div>
  <nav class="footer-nav">
    <span>HOME</span><span>ABOUT US</span><span>WHAT WE DO</span><span>PROPOSED PROJECTS</span><span>TEAM</span><span>CONTACT US</span>
  </nav>
  <p class="copyright">©Copyright information here</p>
</footer>

</body>
</html>
```